Velqor5 Business Card - Health

Velqor5 maximizes value from the health data of its clients, including doctors, HMOs, and patients. I have attached the Velqor5 logo as an ai and eps file.
Target Market(s)
Health, HMO, Healthcare, Data, Big Data, Data Analytics
Industry/Entity Type
Business
Requirements
Must have
- At least one side should have some white on it so that we can write on it.

```html
<!DOCTYPE html>
<html lang="en">
<head>
<meta charset="utf-8">
<title>Velqor5 Business Card</title>
<link href="https://fonts.googleapis.com/css2?family=Questrial&family=Arimo:wght@400;700&display=swap" rel="stylesheet">
<style>
  :root {
    --page-bg: #2a2c2f;
    --card-white: #f4f4f4;
    --card-white-shade: #c9c9c9;
    --ink-dark: #1e1f22;
    --ink-grey: #6a6a6a;
    --brand-blue: #1a8be3;
    --blue-deep: #0b66c9;
    --blue-mid: #1b8fe6;
    --blue-light: #39aef2;
    --ink-light: #ffffff;
  }
  html, body {
    margin: 0;
    padding: 0;
    width: 1200px;
    height: 871px;
    overflow: hidden;
    background: var(--page-bg);
  }
  .canvas {
    position: relative;
    width: 1200px;
    height: 871px;
    display: flex;
    align-items: center;
    justify-content: center;
    gap: 60px;
  }
  .card {
    position: relative;
    width: 520px;
    height: 297px;
    overflow: hidden;
    box-shadow: 0 18px 40px rgba(0,0,0,0.55);
  }
  .card--back {
    background: linear-gradient(135deg, #ffffff 0%, var(--card-white) 45%, var(--card-white-shade) 100%);
  }
  .card--front {
    background: var(--blue-mid);
  }
  .front-art {
    position: absolute;
    inset: 0;
    background: linear-gradient(120deg, var(--blue-deep) 0%, var(--blue-mid) 45%, var(--blue-light) 70%, var(--blue-deep) 100%);
  }
  .brand {
    display: flex;
    align-items: center;
    gap: 14px;
  }
  .brand__dot {
    width: 40px;
    height: 40px;
    border-radius: 50%;
    background: var(--brand-blue);
  }
  .brand__name {
    font-family: "Questrial", sans-serif;
    font-size: 56px;
    line-height: 1;
    color: var(--ink-dark);
    letter-spacing: 1px;
  }
  .card--back .brand {
    position: absolute;
    left: 120px;
    top: 110px;
  }
  .card--back .web {
    position: absolute;
    left: 0;
    right: 0;
    top: 205px;
    text-align: center;
    font-family: "Arimo", sans-serif;
    font-size: 11px;
    letter-spacing: 6px;
    color: var(--ink-grey);
  }
  .card--front .brand {
    position: absolute;
    left: 150px;
    top: 52px;
  }
  .card--front .brand__dot {
    background: var(--blue-deep);
  }
  .contact {
    position: absolute;
    left: 0;
    right: 0;
    top: 150px;
    text-align: center;
    font-family: "Arimo", sans-serif;
    color: var(--ink-light);
  }
  .contact__name {
    font-size: 18px;
    font-weight: 700;
    margin: 0;
  }
  .contact__role {
    font-size: 13px;
    margin: 2px 0 8px;
  }
  .contact__line {
    font-size: 12px;
    font-weight: 700;
    margin: 3px 0;
  }
</style>
</head>
<body>
<main class="canvas">
  <section class="card card--back" aria-label="Card back">
    <div class="brand">
      <span class="brand__dot"></span>
      <span class="brand__name">Velqor5</span>
    </div>
    <div class="web">www.velqor5.com</div>
  </section>

  <section class="card card--front" aria-label="Card front">
    <div class="front-art" role="img" aria-label="Blue faceted geometric background pattern"></div>
    <div class="brand">
      <span class="brand__dot"></span>
      <span class="brand__name">Velqor5</span>
    </div>
    <div class="contact">
      <p class="contact__name">Marten Vale</p>
      <p class="contact__role">President</p>
      <p class="contact__line">2671 Harlow Avenue, Brookfield, NY 10452</p>
      <p class="contact__line">P: 555 0142 7731 &nbsp;M: 555 0187 2264 &nbsp;F: 555 0129 4418</p>
      <p class="contact__line">E: marten@velqor5.com &nbsp;W: www.velqor5.com</p>
    </div>
  </section>
</main>
</body>
</html>
```